Cosmetic injections clinic needs a fresh looking business card

We need a business card using the supplied logo and color scheme to attract future clients to our clinic. It should be modern and fresh, eye catching and not too busy. Simple and to the point is best. I would like two sided designs with the front indicating address and contact information, and the back in full color with white logo and descriptive information also provided.
Target Market(s)
Clients looking for non surgical beauty enhancements.
Contact Information for Business Card
MeloraSkin
14, 618 Birchmont Way
St. Albert, Alberta
K2P 7W3
Phone: 587-412-6630
Email: info@meloraskin.com
Requirements
Must have
- -Logo supplied with the name and address of the clinic
- -Back of card in full color with white logo with A small line of text indicating both of the following: Anti aging consultants and cosmetic injectables
- Located inside the Voyager Wellness Group

```html
<!DOCTYPE html>
<html lang="en">
<head>
<meta charset="utf-8">
<title>MeloraSkin Business Card</title>
<link href="https://fonts.googleapis.com/css2?family=Quicksand:wght@500;600;700&family=Pinyon+Script&display=swap" rel="stylesheet">
<style>
  :root {
    --purple: #5d3a8d;
    --purple-deep: #4f2f7c;
    --pink: #e0418d;
    --teal: #2fb39a;
    --ink: #2e2a36;
    --card-white: #f7f6f8;
    --backdrop: #e9e6ec;
    --white: #ffffff;
  }
  * { margin: 0; padding: 0; box-sizing: border-box; }
  html, body {
    width: 1200px; height: 1200px; overflow: hidden;
    background: var(--backdrop);
    font-family: "Quicksand", sans-serif;
  }
  .sheet {
    position: relative; width: 1200px; height: 1200px;
  }
  .card {
    position: absolute; left: 150px; width: 900px; height: 514px;
    border-radius: 6px; overflow: hidden;
    box-shadow: 0 14px 34px rgba(40, 20, 60, 0.18);
  }
  /* Back side */
  .card-back {
    top: 60px; background: var(--purple);
    display: flex; flex-direction: column; align-items: center; justify-content: center;
  }
  .back-brand {
    display: flex; align-items: center; gap: 22px;
    color: var(--white); font-weight: 700; font-size: 72px; letter-spacing: 1px;
  }
  .brand-dot {
    width: 46px; height: 46px; border-radius: 50%; flex: none;
  }
  .card-back .brand-dot { background: var(--white); }
  .back-email {
    position: absolute; bottom: 56px; left: 0; right: 0; text-align: center;
    color: var(--white); font-weight: 600; font-size: 24px; letter-spacing: 0.5px;
  }
  /* Front side */
  .card-front {
    top: 626px; background: var(--card-white);
    padding: 48px 60px;
  }
  .front-brand {
    display: flex; align-items: center; gap: 16px;
    color: var(--purple); font-weight: 700; font-size: 54px;
  }
  .card-front .brand-dot { width: 34px; height: 34px; background: var(--pink); }
  .tagline {
    margin-top: 12px;
    font-family: "Pinyon Script", cursive;
    color: var(--purple); font-size: 32px;
  }
  .contact-list { list-style: none; margin-top: 26px; }
  .contact-item {
    display: flex; align-items: flex-start; gap: 18px;
    color: var(--ink); font-weight: 700; margin-bottom: 14px;
  }
  .contact-item svg { flex: none; width: 26px; height: 26px; margin-top: 2px; }
  .address { font-size: 21px; line-height: 1.2; }
  .phone { font-size: 30px; letter-spacing: 1px; }
  .email { font-size: 27px; }
  .holder {
    position: absolute; right: 60px; bottom: 52px; text-align: right;
  }
  .holder-name { color: var(--purple); font-weight: 700; font-size: 50px; line-height: 1.05; }
  .holder-title { color: var(--pink); font-weight: 700; font-size: 24px; letter-spacing: 1.5px; }
</style>
</head>
<body>
<main class="sheet">

  <section class="card card-back" aria-label="Card back">
    <div class="back-brand"><span class="brand-dot"></span>MeloraSkin</div>
    <p class="back-email">Email: info@meloraskin.com</p>
  </section>

  <section class="card card-front" aria-label="Card front">
    <div class="front-brand"><span class="brand-dot"></span>MeloraSkin</div>
    <p class="tagline">Anti aging consultants And cosmetic injectables</p>

    <ul class="contact-list">
      <li class="contact-item">
        <svg viewBox="0 0 24 24" aria-hidden="true">
          <path d="M12 2a7 7 0 0 0-7 7c0 5 7 13 7 13s7-8 7-13a7 7 0 0 0-7-7z" fill="none" stroke="var(--pink)" stroke-width="2.4"/>
          <circle cx="12" cy="9" r="2.6" fill="var(--pink)"/>
        </svg>
        <span class="address">14, 618 Birchmont Way<br>St. Albert, Alberta<br>K2P 7W3</span>
      </li>
      <li class="contact-item">
        <svg viewBox="0 0 24 24" aria-hidden="true">
          <path d="M6.6 2.8l2.6 0.3 1.2 4.3-2 1.6c1 2.4 2.8 4.3 5.2 5.4l1.6-2 4.3 1.3 0.3 2.6c-0.2 1.5-1.6 2.7-3.2 2.6C9.6 18.4 5 13.6 4 7c-0.2-1.7 1-3.1 2.6-4.2z" fill="var(--pink)"/>
        </svg>
        <span class="phone">587-412-6630</span>
      </li>
      <li class="contact-item">
        <svg viewBox="0 0 24 24" aria-hidden="true">
          <circle cx="12" cy="12" r="9.5" fill="none" stroke="var(--pink)" stroke-width="2"/>
          <ellipse cx="12" cy="12" rx="4" ry="9.5" fill="none" stroke="var(--pink)" stroke-width="1.8"/>
          <path d="M2.5 12h19M4 7h16M4 17h16" stroke="var(--pink)" stroke-width="1.6"/>
        </svg>
        <span class="email">info@meloraskin.com</span>
      </li>
    </ul>

    <div class="holder">
      <p class="holder-name">Your Name</p>
      <p class="holder-title">Job Title/CEO</p>
    </div>
  </section>

</main>
</body>
</html>
```